Hi,
Brackwell Construction is a domestic builder on the Gold Coast specializing in new homes, townhouses, duplexes and high end renovations.
Brackwell Construction can make your dream new home or development a reality. Whether you already have plans or require a complete design and construct project service, Brackwell Construction will make your project a stress free experience.
We offer design, town planning, certification and construction services.

Target Market(s)

Anyone looking to build.

Industry/Entity Type

Building

Coding

Coded - Design and coding required

Font styles to use
Other font styles liked:
• Match logo

Colors

Designer to choose colors to be used in the design.

Requirements
Must have
• Attractive home page with logo etc.
• About us page
• Gallery page
• Services Page
• Contact us page

```html
<!DOCTYPE html>
<html lang="en">
<head>
<meta charset="utf-8">
<title>Brackwell Construction</title>
<link rel="stylesheet" href="https://fonts.googleapis.com/css2?family=Lato:wght@300;400;700&display=swap">
<style>
:root{
  --black:#000;
  --panel:#0e0e0e;
  --panel-2:#151515;
  --footer:#1b1b1b;
  --white:#fff;
  --text:#e6e6e6;
  --muted:#a9a9a9;
  --line:#cfcfcf;
}
*{box-sizing:border-box;margin:0;padding:0}
html,body{width:1200px;height:4712px;overflow:hidden;background:var(--black)}
body{font-family:"Lato",Arial,sans-serif;color:var(--text);position:relative}
section,header,footer{position:relative;width:1200px;overflow:hidden}
.abs{position:absolute}
.title{position:absolute;left:0;width:1200px;text-align:center;font-size:26px;font-weight:400;color:var(--white);letter-spacing:.5px}
.title::after{content:"";display:block;width:62px;height:2px;background:var(--line);margin:22px auto 0}
.btn{position:absolute;height:38px;border:2px solid var(--white);border-radius:20px;color:var(--white);font-size:12px;letter-spacing:.5px;display:flex;align-items:center;justify-content:center;background:transparent}
.btn.solid{background:var(--white);color:var(--black)}
.lorem{font-size:14px;line-height:19px;color:var(--text)}

/* top bar + header */
.site-header{height:195px;background:var(--black)}
.topbar{position:absolute;top:0;left:0;width:1200px;height:24px;background:#141414;font-size:11px;color:var(--muted)}
.topbar .contact{position:absolute;left:22px;top:5px;display:flex;gap:24px}
.topbar .social{position:absolute;right:22px;top:6px;display:flex;gap:10px}
.topbar .social span{width:12px;height:12px;border-radius:50%;background:#777}
.brand{position:absolute;left:0;width:1200px;top:38px;display:flex;flex-direction:column;align-items:center}
.brand .mark{width:50px;height:50px;border:2px solid var(--white);border-radius:50%}
.brand .name{margin-top:6px;font-size:22px;color:var(--white);font-weight:400}
.brand .tag{font-size:9px;color:var(--muted);letter-spacing:1px}
.nav{position:absolute;top:148px;left:0;width:1200px;display:flex;justify-content:center;gap:50px;font-size:15px;color:var(--white)}
.nav a{color:var(--white);text-decoration:none;position:relative;padding-bottom:10px}
.nav a.active::after{content:"";position:absolute;left:0;right:0;bottom:-8px;height:3px;background:var(--white)}

/* hero */
.hero{height:590px}
.hero-photo{position:absolute;inset:0;
  background:
    linear-gradient(180deg,rgba(0,0,0,.15) 0%,rgba(0,0,0,0) 40%,rgba(0,0,0,.35) 100%),
    radial-gradient(ellipse 170px 130px at 340px 230px,rgba(255,205,120,.85),rgba(255,170,80,.25) 55%,rgba(0,0,0,0) 100%),
    radial-gradient(ellipse 420px 170px at 760px 500px,rgba(205,192,170,.55),rgba(0,0,0,0) 75%),
    linear-gradient(90deg,#1c100b 0%,#3d2216 18%,#5a3322 32%,#3a2317 48%,#2b1d16 58%,#8d8678 70%,#d4cdbd 80%,#9a8f7e 88%,#2c2019 94%,#170f0b 100%)}
.hero-ring{position:absolute;left:375px;top:140px}
.hero-text{position:absolute;left:0;width:1200px;text-align:center;color:var(--white)}
.hero-dots{position:absolute;left:1090px;top:555px;display:flex;gap:7px}
.hero-dots span{width:8px;height:8px;border-radius:50%;background:#888}
.hero-dots span.on{background:var(--white)}

/* specialize */
.specialize{height:384px;background:var(--panel)}
.spec-item{position:absolute;top:145px;width:250px}
.spec-num{position:absolute;left:0;top:0;width:44px;height:44px;border:2px solid var(--white);border-radius:50%;display:flex;align-items:center;justify-content:center;font-size:16px;color:var(--white)}
.spec-item h3{position:absolute;left:56px;top:0;font-size:16px;font-weight:400;color:var(--white);white-space:nowrap}
.spec-item p{position:absolute;left:56px;top:22px;width:180px;font-size:13px;line-height:17px}

/* about */
.about{height:392px;background:var(--black)}
.about h2{position:absolute;left:79px;top:75px;font-size:25px;font-weight:400;color:var(--white)}
.about .lorem{position:absolute;left:79px;width:460px}
.about-photo{position:absolute;left:603px;top:0;width:597px;height:392px;
  background:
    radial-gradient(ellipse 200px 120px at 300px 80px,rgba(235,235,232,.9),rgba(235,235,232,0) 100%),
    radial-gradient(ellipse 260px 120px at 260px 300px,rgba(225,220,210,.9),rgba(225,220,210,0) 100%),
    linear-gradient(180deg,#2b2b2d 0%,#4a4a4c 40%,#6b4f38 75%,#3a2a1e 100%)}

/* services */
.services{height:622px;background:var(--panel-2)}
.services .intro{position:absolute;top:170px;left:0;width:1200px;text-align:center;font-size:14px}
.svc{position:absolute;top:252px;width:240px;text-align:center}
.svc .pic{width:226px;height:226px;border-radius:50%;margin:0 auto}
.svc h3{margin-top:27px;font-size:16px;font-weight:400;color:var(--white)}

/* projects */
.projects{height:848px;background:var(--black)}
.arrows{position:absolute;display:flex;gap:6px}
.arrows span{width:20px;height:20px;border-radius:50%;background:#555;display:flex;align-items:center;justify-content:center}
.arrows span.on{background:var(--white)}
.grid{position:absolute;left:0;top:204px;width:1200px;display:grid;grid-template-columns:repeat(3,1fr);gap:6px}
.grid div{height:248px}

/* blogs */
.blogs{height:761px;background:var(--panel)}
.post{position:absolute;top:167px;width:336px}
.post .pic{height:204px}
.post h3{margin-top:31px;font-size:16px;font-weight:400;color:var(--white)}
.post .meta{margin-top:10px;display:flex;gap:48px;font-size:12px;color:var(--muted)}
.post .lorem{margin-top:6px}
.post .more{margin-top:12px;font-size:12px;color:var(--white);text-decoration:underline}

/* contact */
.contact{height:559px;background:var(--black)}
.field{position:absolute;height:51px;border:2px solid #d8d8d8;border-radius:14px;font-size:11px;color:var(--muted);padding:16px 18px;background:transparent}
.field.area{border-radius:6px}

/* footer */
.site-footer{height:361px;background:var(--footer)}
.foot-brand{position:absolute;left:79px;top:42px}
.foot-brand .mark{width:38px;height:38px;border:2px solid var(--white);border-radius:50%}
.foot-brand .name{font-size:16px;color:var(--white);margin-top:4px}
.foot-col{position:absolute;top:44px}
.foot-col h4{font-size:16px;font-weight:400;color:var(--white)}
.foot-col h4::after{content:"";display:block;width:40px;height:1px;background:var(--muted);margin-top:18px}
.foot-col ul{list-style:none;margin-top:18px;font-size:13px;line-height:19px}
.foot-social{display:flex;gap:8px;margin-top:10px}
.foot-social span{width:16px;height:16px;border-radius:50%;background:#888}
.foot-rule{position:absolute;left:79px;top:298px;width:1042px;height:1px;background:#555}
.foot-bottom{position:absolute;top:322px;font-size:12px;color:var(--text)}
</style>
</head>
<body>

<header class="site-header">
  <div class="topbar">
    <div class="contact"><span>(+061) 555 014 2</span><span>info@brackwellbuild.com</span></div>
    <div class="social"><span></span><span></span><span></span><span></span><span></span></div>
  </div>
  <div class="brand">
    <div class="mark"></div>
    <div class="name">Brackwell</div>
    <div class="tag">construction</div>
  </div>
  <nav class="nav">
    <a class="active" href="#">Home</a><a href="#">About</a><a href="#">Services</a><a href="#">Projects</a><a href="#">Contact</a>
  </nav>
</header>

<section class="hero">
  <div class="hero-photo" role="img" aria-label="Warm lit living room with sofa, cushions, brass lamp and bright window view"></div>
  <svg class="hero-ring" width="420" height="290" viewBox="0 0 420 290"><ellipse cx="210" cy="145" rx="206" ry="141" fill="none" stroke="#fff" stroke-width="2" stroke-dasharray="560 80"/></svg>
  <div class="hero-text" style="top:180px;font-size:36px;font-weight:400">YOUR</div>
  <div class="hero-text" style="top:222px;font-size:52px;font-weight:400;letter-spacing:1px">DREAM HOME</div>
  <div class="hero-text" style="top:297px;font-size:17px">CONSTRUCTIONS &amp; RENOVATIONS</div>
  <div class="btn" style="left:460px;top:347px;width:120px;font-size:11px">READ MORE</div>
  <div class="btn solid" style="left:612px;top:347px;width:120px;font-size:11px">CONTACT US</div>
  <div class="hero-dots"><span></span><span class="on"></span><span></span><span></span></div>
</section>

<section class="specialize">
  <h2 class="title" style="top:60px">OUR SPECIALIZE</h2>
  <div class="spec-item" style="left:79px"><div class="spec-num">01</div><h3>NEW HOMES</h3><p>Lorem Ipsum is simply dummy text of the printing and typesetting industry.</p></div>
  <div class="spec-item" style="left:346px"><div class="spec-num">02</div><h3>TOWN PLANNNING</h3><p>Lorem Ipsum is simply dummy text of the printing and typesetting industry.</p></div>
  <div class="spec-item" style="left:616px"><div class="spec-num">03</div><h3>DUPLEXES</h3><p>Lorem Ipsum is simply dummy text of the printing and typesetting industry.</p></div>
  <div class="spec-item" style="left:886px"><div class="spec-num">04</div><h3>RENOVATIONS</h3><p>Lorem Ipsum is simply dummy text of the printing and typesetting industry.</p></div>
</section>

<section class="about">
  <h2>ABOUT US</h2>
  <p class="lorem" style="top:118px">Lorem Ipsum is simply dummy text of the printing and typesetting industry. Lorem Ipsum has been the industry's standard dummy text ever since the 1500s, when an unknown printer took a galley of type and scrambled it to make a type specimen book.</p>
  <p class="lorem" style="top:224px">It has survived not only five centuries, but also the leap into electronic typesetting, remaining essentially unchanged.</p>
  <div class="btn" style="left:79px;top:286px;width:148px;height:36px">READ MORE</div>
  <div class="about-photo" role="img" aria-label="Builder's hands reviewing construction plans on a wooden desk"></div>
  <svg class="abs" style="left:848px;top:162px" width="68" height="68" viewBox="0 0 68 68"><circle cx="34" cy="34" r="31" fill="none" stroke="#fff" stroke-width="2" opacity=".85"/><path d="M27 22 L47 34 L27 46 Z" fill="none" stroke="#fff" stroke-width="2" opacity=".85"/></svg>
</section>

<section class="services">
  <h2 class="title" style="top:60px">OUR SERVICES</h2>
  <p class="intro">Lorem Ipsum is simply dummy text of the printing and typesetting industry.</p>
  <div class="svc" style="left:75px"><div class="pic" role="img" aria-label="Model of town planning layout with small houses and trees" style="background:radial-gradient(ellipse 90px 60px at 45% 62%,#5f9e3c,#8fc46a 45%,rgba(143,196,106,0) 100%),radial-gradient(circle at 60% 30%,#c9b9a6,rgba(201,185,166,0) 40%),#ecece8"></div><h3>TOWN PLANNNING</h3></div>
  <div class="svc" style="left:345px"><div class="pic" role="img" aria-label="Design drawings with glasses and pencil" style="background:radial-gradient(ellipse 70px 40px at 45% 62%,#3a3a3a,rgba(58,58,58,0) 100%),radial-gradient(circle at 70% 30%,#d8c07a,rgba(216,192,122,0) 35%),linear-gradient(160deg,#fafafa,#d9d9d9)"></div><h3>DESIGN</h3></div>
  <div class="svc" style="left:615px"><div class="pic" role="img" aria-label="Inspector in suit holding a white hard hat" style="background:radial-gradient(ellipse 55px 40px at 62% 62%,#fbfbfb,rgba(251,251,251,0) 100%),linear-gradient(100deg,#e7e7e7 0%,#e7e7e7 25%,#2a2a2c 45%,#3c3c40 70%,#d9d9d9 90%)"></div><h3>CERTIFICATION</h3></div>
  <div class="svc" style="left:885px"><div class="pic" role="img" aria-label="Timber house frame under construction against the sky" style="background:radial-gradient(circle at 50% 55%,#f1e1c8,rgba(241,225,200,0) 55%),linear-gradient(180deg,#e3eef5 0%,#d9a56a 35%,#c88445 65%,#e9cba2 100%)"></div><h3>CONSTRUCTION</h3></div>
</section>

<section class="projects">
  <h2 class="title" style="top:60px">RECENTLY PROJECTS</h2>
  <div class="arrows" style="left:1072px;top:124px">
    <span><svg width="8" height="10" viewBox="0 0 8 10"><path d="M6 1 L2 5 L6 9" fill="none" stroke="#fff" stroke-width="2"/></svg></span>
    <span class="on"><svg width="8" height="10" viewBox="0 0 8 10"><path d="M2 1 L6 5 L2 9" fill="none" stroke="#000" stroke-width="2"/></svg></span>
  </div>
  <div class="grid">
    <div role="img" aria-label="Row of white terrace townhouses under blue sky" style="background:linear-gradient(180deg,#6e9cc9 0%,#a9c6e0 22%,#eef0f2 30%,#d7dbdf 60%,#8a8f94 100%)"></div>
    <div role="img" aria-label="Bright white living room with sofa and floor lamp" style="background:radial-gradient(ellipse 160px 60px at 50% 78%,#dcdad5,rgba(220,218,213,0) 100%),linear-gradient(180deg,#f7f7f6 0%,#ebebe8 60%,#c9c6c0 100%)"></div>
    <div role="img" aria-label="Suburban street with houses and flowering gardens" style="background:linear-gradient(180deg,#b9cfe3 0%,#dfe7ee 28%,#6f7d4f 48%,#b6544a 68%,#9a9a96 85%,#6c6a66 100%)"></div>
    <div role="img" aria-label="Open plan white kitchen and lounge" style="background:radial-gradient(ellipse 120px 70px at 70% 70%,#f2d6d6,rgba(242,214,214,0) 100%),linear-gradient(180deg,#fafaf9 0%,#ecebe8 55%,#cfcac2 100%)"></div>
    <div role="img" aria-label="Colourful apartment facades with balconies" style="background:linear-gradient(90deg,#4f79a8 0%,#6f93bd 35%,#d9a5a0 55%,#e6b7b1 70%,#cfc9bf 85%,#b8b3aa 100%)"></div>
    <div role="img" aria-label="Modern white kitchen with island bench and dark stools" style="background:radial-gradient(ellipse 150px 40px at 55% 88%,#2f2f2f,rgba(47,47,47,0) 100%),linear-gradient(180deg,#f1f1ef 0%,#e2e1de 55%,#b7b5b1 100%)"></div>
  </div>
  <div class="btn" style="left:528px;top:767px;width:144px;height:34px;font-size:11px">VIEW MORE</div>
</section>

<section class="blogs">
  <h2 class="title" style="top:60px">LATEST BLOGS</h2>
  <div class="arrows" style="left:1072px;top:124px">
    <span><svg width="8" height="10" viewBox="0 0 8 10"><path d="M6 1 L2 5 L6 9" fill="none" stroke="#fff" stroke-width="2"/></svg></span>
    <span class="on"><svg width="8" height="10" viewBox="0 0 8 10"><path d="M2 1 L6 5 L2 9" fill="none" stroke="#000" stroke-width="2"/></svg></span>
  </div>
  <article class="post" style="left:79px">
    <div class="pic" role="img" aria-label="Modern house exterior lit at dusk" style="background:radial-gradient(ellipse 60px 50px at 45% 65%,#f0b45c,rgba(240,180,92,0) 100%),linear-gradient(180deg,#4f6f8f 0%,#8aa0b0 35%,#4a4a46 60%,#22201d 100%)"></div>
    <h3>BLOG # 01</h3>
    <div class="meta"><span>13/10/2018</span><span>Comments ( 20 )</span></div>
    <p class="lorem">Lorem Ipsum is simply dummy text of the printing and typesetting industry. Lorem Ipsum has been the industry's standard dummy text ever since the 1500s.</p>
    <div class="more">READ MORE</div>
  </article>
  <article class="post" style="left:434px">
    <div class="pic" role="img" aria-label="White kitchen with black pendant lights" style="background:linear-gradient(180deg,#f5f5f4 0%,#e8e8e6 45%,#bdbbb6 75%,#6a5040 100%)"></div>
    <h3>BLOG # 02</h3>
    <div class="meta"><span>13/10/2018</span><span>Comments ( 35 )</span></div>
    <p class="lorem">Lorem Ipsum is simply dummy text of the printing and typesetting industry. Lorem Ipsum has been the industry's standard dummy text ever since the 1500s.</p>
    <div class="more">READ MORE</div>
  </article>
  <article class="post" style="left:785px">
    <div class="pic" role="img" aria-label="White cottage with red door among autumn trees" style="background:radial-gradient(ellipse 90px 55px at 50% 60%,#f1efea,rgba(241,239,234,0) 100%),linear-gradient(180deg,#d9c9a4 0%,#c8a25e 30%,#a8884f 55%,#7c8b4c 80%,#5e6b3b 100%)"></div>
    <h3>BLOG # 03</h3>
    <div class="meta"><span>13/10/2018</span><span>Comments ( 18 )</span></div>
    <p class="lorem">Lorem Ipsum is simply dummy text of the printing and typesetting industry. Lorem Ipsum has been the industry's standard dummy text ever since the 1500s.</p>
    <div class="more">READ MORE</div>
  </article>
  <div class="btn" style="left:528px;top:657px;width:144px;height:34px;font-size:11px">VIEW MORE</div>
</section>

<section class="contact">
  <h2 class="title" style="top:40px">CONTACT US</h2>
  <div class="field" style="left:79px;top:166px;width:340px">FULL NAME</div>
  <div class="field" style="left:434px;top:166px;width:336px">EMAIL ADDRESS</div>
  <div class="field" style="left:779px;top:166px;width:339px">PHONE NUMBER</div>
  <div class="field area" style="left:79px;top:232px;width:1039px;height:173px">MESSAGE</div>
  <div class="btn" style="left:83px;top:431px;width:144px;height:34px;font-size:11px">VIEW MORE</div>
</section>

<footer class="site-footer">
  <div class="foot-brand">
    <div class="mark"></div>
    <div class="name">Brackwell</div>
    <p class="lorem" style="margin-top:22px;width:260px;font-size:13px;line-height:17px">Lorem Ipsum is simply dummy text of the printing and typesetting industry.</p>
    <div style="margin-top:6px;font-size:12px;color:#fff;text-decoration:underline">READ MORE</div>
    <div class="foot-social"><span></span><span></span><span></span><span></span><span></span></div>
  </div>
  <div class="foot-col" style="left:446px">
    <h4>QUICK LINK</h4>
    <ul><li>Home</li><li>About</li><li>Services</li><li>Projects</li><li>Contact</li></ul>
  </div>
  <div class="foot-col" style="left:657px">
    <h4>NEWSLETTER</h4>
    <p style="margin-top:18px;width:190px;font-size:13px;line-height:17px">Lorem Ipsum is simply dummy text of the printing.</p>
    <div style="margin-top:8px;width:182px;height:22px;border:1px solid #fff;border-radius:11px;font-size:10px;padding:4px 10px;color:#ccc">Email</div>
    <div style="margin-top:6px;width:100px;height:22px;border-radius:11px;background:#fff;color:#000;font-size:10px;display:flex;align-items:center;justify-content:center">SUBSCRIBE</div>
  </div>
  <div class="foot-col" style="left:889px">
    <h4>QUICK LINK</h4>
    <ul style="font-size:12px;line-height:19px">
      <li>&#9742;&nbsp; (+061)-555-014-2</li>
      <li>&#9742;&nbsp; (+061)-555-014-2</li>
      <li>&#9993;&nbsp; info@brackwellbuild.com</li>
      <li>&#9906;&nbsp; 48 Harbour Lane,</li>
      <li>&nbsp;&nbsp;&nbsp;&nbsp;Southport QLD 4215</li>
    </ul>
  </div>
  <div class="foot-rule"></div>
  <div class="foot-bottom" style="left:79px">Copyright © 2018 Brackwell construction. All rights reserved.</div>
  <div class="foot-bottom" style="left:897px">Privacy Policy - Terms &amp; conditions</div>
</footer>

</body>
</html>
```